National online rug retailer needs a home page design

See the LoomNest logo and create a home page design around that color theme. Details are spelled out in word document uploaded below.
Updates

Apparently this website did not take my attachement showing the logo and basic requirements.  If you would send me your email address, I will send you the attachment directly.
Best regards,
Ned Carver
ncarver@qwplex.com

Target Market(s)

The target market is home owners 25 to 75 years old with combined incomes over $100,000 per year.

Industry/Entity Type

Online

Requirements
Must have
• Lots of white space with black letters and creative use of red and possibly one other color. Would like a compelling call to action button.

```html
<!DOCTYPE html>
<html lang="en">
<head>
<meta charset="utf-8">
<title>LoomNest — Home</title>
<link rel="stylesheet" href="https://fonts.googleapis.com/css2?family=Roboto:ital,wght@0,400;0,500;0,700;1,400&display=swap">
<style>
:root{
  --red:#c8141c;
  --red-dark:#a50f16;
  --ink:#222;
  --text:#555;
  --muted:#888;
  --line:#dedede;
  --page:#eeeeee;
  --white:#fff;
  --nav:#3a3a3a;
  --nav-dark:#2a2a2a;
  --orange:#f39a14;
  --green:#3aa02a;
  --card:#2e2e2e;
}
*{box-sizing:border-box;margin:0;padding:0}
html,body{width:1200px;height:1191px;overflow:hidden;background:var(--page);font-family:"Roboto",Arial,sans-serif;color:var(--ink)}
.stage{position:relative;width:1200px;height:1191px;overflow:hidden;background:var(--page)}
.abs{position:absolute}
ul{list-style:none}

/* main sheet */
.sheet{left:131px;top:0;width:938px;height:868px;background:var(--white);box-shadow:0 1px 3px rgba(0,0,0,.08)}
.logo{left:131px;top:42px;display:flex;align-items:center;gap:7px;white-space:nowrap}
.logo-mark{width:18px;height:18px;background:var(--red);flex:none}
.logo-name{font-size:29px;font-weight:500;color:var(--red);letter-spacing:-.3px;line-height:1}
.tagline{left:197px;top:81px;font-size:10px;color:var(--muted);white-space:nowrap}

.search{left:376px;top:22px;width:347px;height:80px;border:1px solid var(--line);background:#fbfbfb;padding:8px 18px}
.search .account{font-size:11px;color:var(--text)}
.search .field{position:absolute;left:18px;top:28px;width:264px;height:38px;border:1px solid #ccc;background:#fff;font-size:13px;color:var(--muted);padding:10px 12px}
.search .go{position:absolute;right:18px;top:28px;width:40px;height:40px;background:var(--orange);border:1px solid #d88000}

.cart{left:749px;top:0;width:320px;height:99px;background:var(--red);border-bottom:3px solid var(--red-dark)}
.cart .tab{position:absolute;left:21px;top:0;width:50px;height:76px;background:#3a3a3a;color:#fff;font-size:11px;text-align:center;padding-top:36px}
.cart .tab svg{position:absolute;left:15px;top:12px}
.cart .links{position:absolute;left:86px;top:17px;font-size:12px;color:#fff;display:flex;gap:22px}
.cart .order{position:absolute;left:86px;top:44px;font-size:12px;color:#fff}
.cart .phone{position:absolute;left:86px;top:58px;font-size:24px;font-weight:500;color:#fff}

.nav{left:131px;top:128px;width:812px;height:41px;background:var(--nav);display:flex;align-items:center;padding-left:10px}
.nav a{color:#fff;text-decoration:none;font-size:15px;padding:0 14px;border-right:1px solid #555;line-height:41px}
.nav a:last-child{border-right:0}
.chat{left:928px;top:124px;width:141px;height:50px;background:var(--green);color:#fff;font-size:12px;font-weight:700;text-align:center;padding-top:30px;clip-path:polygon(10px 0,100% 0,100% 100%,10px 100%,0 50%)}
.chat svg{position:absolute;left:61px;top:8px}

/* section titles */
.h-title{display:flex;align-items:center;gap:8px;font-size:15px;font-weight:500;color:var(--ink)}
.dot{width:15px;height:15px;border-radius:50%;border:2px solid var(--red);position:relative}
.dot::after{content:"";position:absolute;left:3px;top:3px;width:5px;height:5px;border-radius:50%;background:var(--red)}

/* browse */
.browse{left:150px;top:192px;width:167px;height:298px;border:1px solid var(--line)}
.browse .h-title{padding:10px 12px;border-bottom:1px solid var(--line)}
.browse li{display:flex;justify-content:space-between;align-items:center;font-size:11px;color:var(--text);padding:0 12px;height:22px}
.browse li .lbl::before{content:"⊕";color:#999;margin-right:8px}
.browse li .sign{color:#aaa}
.browse .sub{padding-left:38px;font-size:11px;color:#777;height:19px;display:flex;align-items:center}
.browse .sub.on{background:var(--orange);color:#fff}

.promo{left:150px;top:504px;width:167px;height:328px;background:linear-gradient(180deg,#e08a10 0%,#c45e06 55%,#3a3a3a 80%,#d8d8d8 100%)}
.promo .lead{position:absolute;left:16px;top:22px;color:#fff;font-weight:700;line-height:1.05}
.promo .lead span{display:block}

/* hero */
.hero{left:337px;top:192px;width:523px;height:382px;border:1px solid var(--line)}
.hero .photo{position:absolute;left:0;top:0;width:521px;height:292px;background:linear-gradient(180deg,#e9e6e0 0%,#d8d2c8 55%,#b3262a 75%,#8e1a1e 100%)}
.hero .thumbs{position:absolute;left:0;top:292px;width:521px;height:88px;display:flex;align-items:center;justify-content:center;gap:28px}
.arrow{width:24px;height:24px;border-radius:50%;background:#ddd;display:flex;align-items:center;justify-content:center}
.thumb{width:114px;height:60px;border:1px solid var(--line);padding:3px}
.thumb div{width:100%;height:100%}

/* features */
.features-title{left:337px;top:594px}
.rule{position:absolute;height:1px;background:var(--line)}
.feature{top:633px;width:247px;height:88px;background:var(--card);padding:10px}
.feature .pic{position:absolute;left:10px;top:10px;width:68px;height:68px}
.feature h4{position:absolute;left:92px;top:9px;color:#fff;font-size:11px;font-weight:500}
.feature ul{position:absolute;left:92px;top:26px}
.feature li{color:#eee;font-size:11px;font-style:italic;line-height:17px;display:flex;gap:6px;align-items:center}

.about-title{left:337px;top:739px}
.about{left:337px;top:774px;width:530px;font-size:11px;line-height:17px;color:var(--text)}
.about a{color:var(--red);text-decoration:none}

/* also like */
.also{left:880px;top:192px;width:171px;height:645px;border:1px solid var(--line)}
.also .h-title{padding:10px 12px;font-size:14px}
.also-item{position:absolute;left:10px;width:149px;height:140px;border:1px solid var(--line);padding:4px}
.also-item .pic{height:88px}
.also-item p{font-size:10px;color:var(--muted);text-align:center;line-height:14px;margin-top:5px}

/* footer */
.footer{left:131px;top:894px;width:938px;height:250px;background:var(--white);border-top:3px solid #333}
.fcol{top:925px}
.fcol h5{font-size:12px;font-weight:500;color:var(--red);margin-bottom:10px}
.fcol li{font-size:11px;color:var(--text);line-height:17px}
.cards{left:722px;top:924px;display:flex;gap:6px}
.cards span{width:52px;height:30px;border:1px solid #ccc;border-radius:3px}
.badges{left:722px;top:974px;width:333px;height:64px;background:#f1f1f1;display:flex;align-items:center;gap:14px;padding-left:12px}
.badges span{height:34px;background:#d5d5d5;border-radius:3px}
.copy{left:722px;top:1049px;font-size:10px;color:var(--muted)}
</style>
</head>
<body>
<div class="stage">

  <div class="abs sheet"></div>

  <!-- header -->
  <div class="abs logo"><span class="logo-mark"></span><span class="logo-name">LoomNest.com</span></div>
  <div class="abs tagline">for domestic and heirloom values</div>

  <div class="abs search">
    <div class="account">My Account &nbsp;/&nbsp; Sign In</div>
    <div class="field">Enter key words or item</div>
    <div class="go"><svg width="40" height="40" viewBox="0 0 40 40"><circle cx="18" cy="18" r="6" fill="none" stroke="#333" stroke-width="2.5"/><line x1="22.5" y1="22.5" x2="27" y2="27" stroke="#333" stroke-width="3" stroke-linecap="round"/></svg></div>
  </div>

  <div class="abs cart">
    <div class="tab">
      <svg width="20" height="16" viewBox="0 0 20 16"><path d="M1 2h3l2 9h10l2-7H5" fill="none" stroke="#fff" stroke-width="1.6"/><circle cx="8" cy="14" r="1.5" fill="#fff"/><circle cx="15" cy="14" r="1.5" fill="#fff"/></svg>
      Item 3
    </div>
    <div class="links"><span>Total $0.00</span><span>View Cart</span><span>Checkout</span></div>
    <div class="order">Order toll-free:</div>
    <div class="phone">1-888-555-0142</div>
  </div>

  <nav class="abs nav">
    <a>Home</a><a>Selection guides</a><a>Rug Care</a><a>FAQ</a><a>Return Policy</a><a>Free Shipping</a><a>Clearance Rugs</a>
  </nav>
  <div class="abs chat">
    <svg width="20" height="18" viewBox="0 0 20 18"><path d="M2 2h16v10H8l-4 4v-4H2z" fill="#fff"/></svg>
    LIVE CHAT ONLINE
  </div>

  <!-- browse -->
  <aside class="abs browse">
    <div class="h-title"><span class="dot"></span>Browse</div>
    <ul style="padding-top:6px">
      <li><span class="lbl">RUG THEME</span><span class="sign">—</span></li>
      <li class="sub">› Traditional</li>
      <li class="sub on">› Transitional</li>
      <li class="sub">› Casual</li>
      <li style="margin-top:6px"><span class="lbl">COLOR WAY</span><span class="sign">+</span></li>
      <li><span class="lbl">SIZE</span><span class="sign">+</span></li>
      <li><span class="lbl">SHAPE</span><span class="sign">+</span></li>
      <li><span class="lbl">FIBER CONTENT</span><span class="sign">+</span></li>
      <li><span class="lbl">MFGR. BRAND</span><span class="sign">+</span></li>
      <li><span class="lbl">MFGR.COLLECTION</span><span class="sign">+</span></li>
      <li><span class="lbl">PRICE</span><span class="sign">+</span></li>
    </ul>
  </aside>

  <div class="abs promo" role="img" aria-label="Promotional photo of a patterned rug beneath a white chair, with a special offer tag">
    <div class="lead"><span style="font-size:22px">BEST RUG</span><span style="font-size:30px">FOR</span><span style="font-size:15px">THE HOME</span></div>
  </div>

  <!-- hero -->
  <section class="abs hero">
    <div class="photo" role="img" aria-label="Woman relaxing on a red patterned rug in a living room beside a sofa"></div>
    <div class="thumbs">
      <span class="arrow"><svg width="10" height="10" viewBox="0 0 10 10"><path d="M6.5 1.5L3 5l3.5 3.5" fill="none" stroke="#fff" stroke-width="2"/></svg></span>
      <div class="thumb"><div role="img" aria-label="Folded woven rug" style="background:linear-gradient(135deg,#e9e4dc,#7a8fa8 60%,#b34a3a)"></div></div>
      <div class="thumb"><div role="img" aria-label="Stack of colourful rugs" style="background:linear-gradient(135deg,#3b5f8a,#c0402e 50%,#d9a441)"></div></div>
      <div class="thumb"><div role="img" aria-label="Bordered cream rug" style="background:linear-gradient(135deg,#8c2b1f,#e8dcc4 45%,#8c2b1f)"></div></div>
      <span class="arrow"><svg width="10" height="10" viewBox="0 0 10 10"><path d="M3.5 1.5L7 5 3.5 8.5" fill="none" stroke="#fff" stroke-width="2"/></svg></span>
    </div>
  </section>

  <!-- features -->
  <h3 class="abs h-title features-title"><span class="dot"></span>Feature Products</h3>
  <div class="rule" style="left:500px;top:603px;width:360px"></div>

  <article class="abs feature" style="left:337px">
    <div class="pic" role="img" aria-label="Orange and brown patterned rug" style="background:linear-gradient(135deg,#e2c08a,#8a4a22)"></div>
    <h4>LOREM IPSUM IS SIMPLY</h4>
    <ul>
      <li><svg width="10" height="9" viewBox="0 0 10 9"><path d="M1 5l3 3 5-7" fill="none" stroke="#f39a14" stroke-width="2"/></svg>Dummy text of the</li>
      <li><svg width="10" height="9" viewBox="0 0 10 9"><path d="M1 5l3 3 5-7" fill="none" stroke="#f39a14" stroke-width="2"/></svg>And typesetting industry.</li>
      <li><svg width="10" height="9" viewBox="0 0 10 9"><path d="M1 5l3 3 5-7" fill="none" stroke="#f39a14" stroke-width="2"/></svg>Lorem Ipsum has been</li>
    </ul>
  </article>
  <article class="abs feature" style="left:611px">
    <div class="pic" role="img" aria-label="Brown and cream animal print rug" style="background:linear-gradient(135deg,#efe3cc,#6b4224)"></div>
    <h4>LOREM IPSUM IS SIMPLY</h4>
    <ul>
      <li><svg width="10" height="9" viewBox="0 0 10 9"><path d="M1 5l3 3 5-7" fill="none" stroke="#f39a14" stroke-width="2"/></svg>Dummy text of the</li>
      <li><svg width="10" height="9" viewBox="0 0 10 9"><path d="M1 5l3 3 5-7" fill="none" stroke="#f39a14" stroke-width="2"/></svg>And typesetting industry.</li>
      <li><svg width="10" height="9" viewBox="0 0 10 9"><path d="M1 5l3 3 5-7" fill="none" stroke="#f39a14" stroke-width="2"/></svg>Lorem Ipsum has been</li>
    </ul>
  </article>

  <h3 class="abs h-title about-title"><span class="dot"></span>LoomNest</h3>
  <div class="rule" style="left:450px;top:748px;width:410px"></div>
  <p class="abs about">There are many variations of passages of Lorem Ipsum available, but the majority have suffered alteration in some form, by injected humour, or randomised words which don't look even slightly believable. If you are going to use a passage of Lorem Ipsum, you need to be sure there isn't anything embarrassing hidden in the middle of text. All the Lorem Ipsum generators on.. <a>Much more..</a></p>

  <!-- also like -->
  <aside class="abs also">
    <div class="h-title"><span class="dot"></span>You may also like</div>
    <div class="also-item" style="top:44px"><div class="pic" role="img" aria-label="Round pink and red floral rug" style="background:radial-gradient(circle,#f4d9d9,#d24a6a 55%,#f3f3f3 72%)"></div><p>It is a long established fact that a reader will</p></div>
    <div class="also-item" style="top:189px"><div class="pic" role="img" aria-label="Brown giraffe pattern rug" style="background:linear-gradient(135deg,#6b3a1c,#e6d3b3 50%,#6b3a1c)"></div><p>It is a long established fact that a reader will</p></div>
    <div class="also-item" style="top:334px"><div class="pic" role="img" aria-label="Round orange swirl rug" style="background:radial-gradient(circle,#f0c060,#c14a18 50%,#3a1a10 80%)"></div><p>It is a long established fact that a reader will</p></div>
    <div class="also-item" style="top:479px"><div class="pic" role="img" aria-label="Traditional rug laid on a wooden floor" style="background:linear-gradient(135deg,#c9a27a,#8a2a1c 55%,#d8c0a0)"></div><p>It is a long established fact that a reader will</p></div>
  </aside>

  <!-- footer -->
  <footer class="abs footer"></footer>
  <div class="abs fcol" style="left:157px">
    <h5>CUSTOMER SERVICE</h5>
    <ul><li>Shipping</li><li>Return Policy</li><li>Privacy Policy</li><li>Ordering &amp; Delivery Checklist</li><li>Terms of Use</li><li>Terms of Sale</li><li>Contact Us</li><li>Environmental Policy</li></ul>
  </div>
  <div class="abs fcol" style="left:364px">
    <h5>RESOURCES</h5>
    <ul><li>Product Articles</li><li>Learning Center</li><li>Help</li><li>Refer A Friend</li><li>LoomNest Blog</li><li>Room Scene Viewer</li><li>Site Map</li><li>FAQ</li><li>Customer Testimonials</li><li>Photo Gallery</li></ul>
  </div>
  <div class="abs fcol" style="left:530px">
    <h5>CORPORATE INFO</h5>
    <ul><li>About LoomNest.com</li><li>Careers</li><li>Affiliates</li></ul>
  </div>
  <div class="abs cards" aria-label="Accepted payment methods">
    <span style="background:#3b7ac0"></span><span style="background:#2a4f9a"></span><span style="background:#f4f4f4"></span><span style="background:#e8eef6"></span><span style="background:#f4f4f4;width:76px"></span>
  </div>
  <div class="abs badges" aria-label="Security badges">
    <span style="width:36px;border-radius:50%;background:#d9c35a"></span>
    <span style="width:36px;border-radius:50%;background:#d9c35a"></span>
    <span style="width:56px"></span>
    <span style="width:56px;background:#c9d6e6"></span>
    <span style="width:56px"></span>
  </div>
  <div class="abs copy">Copyright 2002 - 2013 by Hartwell LLC. All rights reserved.</div>

</div>
</body>
</html>
```